Ridgeline Build Network Inc. Letterhead

Creation of attractive and eye catching letterhead for a business start-up for the construction industry. Letterhead must relate to construction, but avoid standard hammer and tools in the design.

I forgot to add some details, sorry about that. Some pertinent info: Ph: 916-555-0187 ridgelinebuildnet.example 274 Marrowell Ave, Ste 300 Folsom, CA 95999 info@ridgelinebuildnet.example not sure if slogan should be in there" “Connecting construction professionals to create a purpose driven industry.” must be able to be used in word. Thanks!

```html
<!DOCTYPE html>
<html lang="en">
<head>
<meta charset="utf-8">
<title>Ridgeline Build Network Inc. — Letterhead</title>
<link rel="stylesheet" href="https://fonts.googleapis.com/css2?family=Open+Sans:wght@400;600;700&display=swap">
<style>
  :root {
    --navy: #0f1a52;
    --red: #c0141c;
    --ink: #2b2b2b;
    --muted: #555a66;
    --rule: #c9ccd4;
    --paper: #ffffff;
    --backdrop: #ececec;
  }
  * { box-sizing: border-box; margin: 0; padding: 0; }
  html, body { width: 1200px; height: 784px; overflow: hidden; }
  body {
    background: var(--backdrop);
    font-family: "Open Sans", Arial, sans-serif;
    color: var(--ink);
    position: relative;
  }
  .letterhead {
    position: absolute;
    left: 318px; top: 24px;
    width: 564px; height: 736px;
    background: var(--paper);
    box-shadow: 0 4px 18px rgba(0,0,0,0.12);
    overflow: hidden;
  }
  .edge-stripes { position: absolute; left: 0; top: 0; width: 40px; height: 736px; }
  .brand {
    position: absolute; left: 52px; top: 48px;
    display: flex; align-items: center; gap: 8px;
  }
  .brand-mark { width: 12px; height: 12px; background: var(--red); flex: none; }
  .brand-name {
    font-size: 12px; font-weight: 700; color: var(--navy);
    letter-spacing: 0.3px; line-height: 1.25; white-space: nowrap;
  }
  .contact {
    position: absolute; left: 390px; top: 40px;
    border-left: 1px solid var(--rule);
    padding: 2px 0 2px 9px;
    font-size: 7.5px; line-height: 1.6; color: var(--muted);
    list-style: none;
  }
  .contact li { display: flex; align-items: center; gap: 5px; white-space: nowrap; }
  .contact svg { width: 7px; height: 7px; flex: none; }
  .contact .addr { padding-left: 12px; }
  .letter-body {
    position: absolute; left: 70px; top: 150px; width: 410px;
    font-size: 9.6px; line-height: 1.5; color: var(--ink);
  }
  .salutation { font-weight: 700; font-size: 11.5px; margin-bottom: 12px; color: #333; }
  .letter-body p { margin-bottom: 12px; }
  .signature {
    margin-top: 14px; width: 130px; height: 52px;
    background: linear-gradient(90deg, #f1f1f1, #e2e2e2);
    border-radius: 3px;
  }
</style>
</head>
<body>
  <article class="letterhead">
    <svg class="edge-stripes" viewBox="0 0 40 736" aria-hidden="true">
      <rect x="0" y="0" width="14" height="736" fill="var(--navy)"/>
      <path d="M19 0 L25 0 L22 640 Z" fill="var(--red)"/>
    </svg>

    <header class="brand">
      <span class="brand-mark"></span>
      <span class="brand-name">Ridgeline Build Network Inc.</span>
    </header>

    <ul class="contact">
      <li><svg viewBox="0 0 10 10"><path d="M2 1 L4 1 L5 3 L3.8 4 Q4.8 6 6 6.2 L7 5 L9 6 L9 8 Q5 9 2 5 Q1 3 2 1Z" fill="var(--red)"/></svg>916-555-0187</li>
      <li><svg viewBox="0 0 10 10"><rect x="1" y="2" width="8" height="6" fill="var(--red)"/><path d="M1 2 L5 5.5 L9 2" stroke="#fff" stroke-width="0.9" fill="none"/></svg>info@ridgelinebuildnet.example</li>
      <li><svg viewBox="0 0 10 10"><circle cx="5" cy="5" r="4" fill="var(--red)"/><path d="M1 5 H9 M5 1 Q2.5 5 5 9 M5 1 Q7.5 5 5 9" stroke="#fff" stroke-width="0.6" fill="none"/></svg>ridgelinebuildnet.example</li>
      <li class="addr">274 Marrowell Ave, Ste 300</li>
      <li class="addr">Folsom, CA 95999</li>
    </ul>

    <section class="letter-body">
      <p class="salutation">Dear Mr. Hale,</p>
      <p>Lorem Ipsum is simply dummy text of the printing and typesetting industry. Lorem Ipsum has been the industry's standard dummy text ever since the 1500s, when an unknown printer took a galley of type and scrambled it to make a type specimen book. It has survived not only five centuries, but also the leap into electronic typesetting, remaining essentially unchanged.</p>
      <p>The standard chunk of Lorem Ipsum used since the 1500s is reproduced below for those interested. Sections 1.10.32 and 1.10.33 from "Notes on Steel and Stone" by Alden Voss are also reproduced in their exact original form, accompanied by English versions from the 1914 translation by M. Tierney.</p>
      <p>Lorem Ipsum is simply dummy text of the printing and typesetting industry. Lorem Ipsum has been the industry's standard dummy text ever since the 1500s, when an unknown printer took a galley of type and scrambled it to make a type specimen book. It has survived not only five centuries, but also the leap into electronic typesetting, remaining essentially unchanged. It was popularised in the</p>
      <p>Lorem Ipsum is simply dummy text of the printing and typesetting industry. Lorem Ipsum has been the industry's standard dummy text ever since the 1500s, when an unknown printer took a galley of type and scrambled it to make a type specimen book. It has survived not only five centuries, but also the leap into electronic typesetting, remaining essentially unchanged. It was popularised in the</p>
      <div class="signature" role="img" aria-label="Handwritten signature of the sender"></div>
    </section>
  </article>
</body>
</html>
```